Box design for superfood powders

Hey,
I am creating a new brand of superfoods mixes in and I am looking for a designer to create the design for the box.
I have for 4 products on the roadmap, but I need the design just for the first one:
- For skin nails and hair benefits: Collagen + CoQ10 and Vitamin C powders (eg: Blueberries, Camu Camu, Acai)
- For energy and immune system (eg: mushrooms powder)
- Green Mix (eg: Spirulina + Wheatgrass + Chlorella)
- Protein mix (eg: hemp + rice powders)
I will use Kraft paper for the box so I am able to print max 2 colors on them (black and another color distinctive for each specific powder mix).
I need the design just for the first one with collagen, because all the products will have the same format. I will just change the name, ingredients and the color
More details in the archive attached.

Updates
Low design quality
Target Market(s)
woman between 30-50
Requirements
Should not have
- Ilustrations with fruits or flowers
Just shapes and colors

```html
<!DOCTYPE html>
<html lang="en">
<head>
<meta charset="utf-8">
<title>Lumora Radiant Collagen – Box Layout</title>
<link href="https://fonts.googleapis.com/css2?family=Arimo:wght@700&family=Poppins:ital,wght@0,400;0,500;0,600;0,700;1,400;1,500&display=swap" rel="stylesheet">
<style>
  :root {
    --plum: #744672;
    --plum-deep: #521a52;
    --ink: #111111;
    --frame: #5a5558;
    --heading: #4a4548;
    --paper: #ffffff;
  }
  * { margin: 0; padding: 0; box-sizing: border-box; }
  html, body { width: 1200px; height: 847px; overflow: hidden; background: var(--paper); }
  body { position: relative; font-family: "Poppins", sans-serif; color: var(--ink); }

  .side-title {
    position: absolute; top: 58px; width: 300px; text-align: center;
    font-family: "Arimo", sans-serif; font-weight: 700; font-size: 45px;
    color: var(--heading); text-decoration: underline; text-decoration-thickness: 3px;
    text-underline-offset: 4px; line-height: 1;
  }
  .side-title--front { left: 194px; }
  .side-title--back { left: 699px; }

  .panel {
    position: absolute; top: 152px; width: 419px; height: 593px;
    border: 2px solid var(--frame); background: var(--paper);
  }
  .panel--front { left: 133px; }
  .panel--back { left: 638px; }

  /* Front */
  .brand-block {
    position: absolute; left: 94px; top: -2px; width: 236px; height: 203px;
    background: var(--plum); color: var(--paper); text-align: center;
  }
  .brand-name {
    position: absolute; left: 0; right: 0; top: 18px;
    font-weight: 600; font-size: 72px; line-height: 1; letter-spacing: -2px;
  }
  .brand-tagline {
    position: absolute; left: 0; right: 0; top: 116px;
    font-size: 31px; line-height: 31px; letter-spacing: -0.3px;
  }
  .product-box {
    position: absolute; left: 94px; top: 201px; width: 236px; height: 157px;
    border: 2px solid var(--plum); border-top: none; text-align: center;
  }
  .product-line {
    position: absolute; left: -4px; right: -4px; top: 20px;
    font-size: 55px; line-height: 1; letter-spacing: -1px;
  }
  .product-name {
    position: absolute; left: -4px; right: -4px; top: 80px;
    font-weight: 700; font-size: 51px; line-height: 1; letter-spacing: -1px; color: var(--plum-deep);
  }
  .benefit {
    position: absolute; left: 94px; top: 417px; width: 233px; height: 81px;
    border-top: 2px solid var(--plum-deep); border-bottom: 2px solid var(--plum-deep);
    text-align: center; font-style: italic; font-size: 26px; line-height: 28px; padding-top: 10px;
  }

  /* Back */
  .intro {
    position: absolute; left: 40px; top: 34px; width: 335px; text-align: center;
    font-style: italic; font-size: 14.5px; line-height: 22.6px;
  }
  .ingredients {
    position: absolute; left: 38px; top: 219px; width: 164px; height: 158px;
    border: 2px solid var(--plum); text-align: center;
  }
  .box-header {
    background: var(--plum); color: #2a1a2a; font-weight: 500; line-height: 1;
  }
  .ingredients .box-header { height: 26px; font-size: 20px; padding-top: 3px; }
  .ingredient-list { list-style: none; padding-top: 5px; font-size: 12.5px; line-height: 13px; }
  .ingredient-list li:nth-child(odd) { color: var(--plum); }
  .nutrition {
    position: absolute; left: 53px; top: 392px; width: 136px; height: 129px;
    border: 2px solid var(--plum);
  }
  .nutrition .box-header { height: 23px; font-size: 16px; padding-top: 3px; text-align: center; }
  .nutrition-row { height: 17.6px; border-bottom: 1px solid var(--plum); }
  .nutrition-row:last-child { border-bottom: none; }
  .net-weight {
    position: absolute; left: 30px; top: 535px; width: 180px; text-align: center;
    font-weight: 600; font-size: 15px; color: var(--plum-deep);
  }
  .info { position: absolute; left: 234px; width: 180px; font-size: 10.5px; line-height: 15px; }
  .info h3 { font-size: 10.5px; font-weight: 600; }
  .free-from { top: 217px; font-style: italic; font-size: 13.5px; line-height: 15px; }
  .free-from h3 { font-size: 13.5px; font-weight: 500; }
  .how-to { top: 324px; }
  .storage { top: 400px; }
  .producer { top: 445px; }
  .connect { top: 491px; }
  .accent { color: var(--plum-deep); font-weight: 600; font-size: 11.5px; }
</style>
</head>
<body>
  <h1 class="side-title side-title--front">FRONT</h1>
  <h1 class="side-title side-title--back">BACK</h1>

  <section class="panel panel--front">
    <div class="brand-block">
      <div class="brand-name">lumora</div>
      <div class="brand-tagline">Supercharge<br>your greatness</div>
    </div>
    <div class="product-box">
      <div class="product-line">Radiant</div>
      <div class="product-name">Collagen</div>
    </div>
    <p class="benefit">For skin nails and<br>hair benefits</p>
  </section>

  <section class="panel panel--back">
    <p class="intro">We make it easy for busy people to look and feel good about their appearance. Just add Radiant Collagen powder to your favorite smoothie or milk and get the extra dose of collagen and skin protectingantioxidants. It helps combat the effects of free radicals and may restore your natural plumpness.</p>

    <div class="ingredients">
      <div class="box-header">Ingredients:</div>
      <ul class="ingredient-list">
        <li>Type 1 Marine Collagen</li>
        <li>CoQ10</li>
        <li>Hyaluronic acid powder</li>
        <li>Camu Camu</li>
        <li>Rosehip</li>
        <li>Sea buckthorn</li>
        <li>Banana</li>
        <li>Date</li>
        <li>Acai</li>
      </ul>
    </div>

    <div class="nutrition">
      <div class="box-header">Nutrition Value</div>
      <div class="nutrition-row"></div>
      <div class="nutrition-row"></div>
      <div class="nutrition-row"></div>
      <div class="nutrition-row"></div>
      <div class="nutrition-row"></div>
      <div class="nutrition-row"></div>
    </div>
    <p class="net-weight">14 portions x 10g = 140g</p>

    <div class="info free-from">
      <h3>Free from:</h3>
      <p>Gluten, Dairy, Soy, GMO, sweeteners, fillers, additives, preservatives or anything artificial.</p>
    </div>
    <div class="info how-to">
      <h3>How to use it:</h3>
      <p>Add one pack to your water, smoothies, yoghurt, musli, oatmeal</p>
    </div>
    <div class="info storage">
      <h3>Storage:</h3>
      <p>Keep closed in a cool dry place</p>
    </div>
    <div class="info producer">
      <h3>Produced by.</h3>
      <p>Norvel SRL for Brightpath SRL</p>
    </div>
    <div class="info connect">
      <h3>Connect:</h3>
      <p class="accent">Call +40 111 2222 333</p>
      <p>or visit our website</p>
      <p class="accent">www.lumora.com/ro/start</p>
    </div>
  </section>
</body>
</html>
```